Medical Device Packaging Project 2 of 5

We are a medical device startup company needing packaging for a total of 5 device brands. This is posting 2 of 5 and the device name is "Venmira"

Venmira is an intraocular lens for use in cataract surgery. The target market is Chinese ophthalmologists. The box should be sophisticated and upmarket.

The company name is Tordel Vision, I have included the logo in the uploaded files section. You should include the logo on the box.

I have uploaded a sample lens boxes from other companies that demonstrate the information needed to be contained on the box in terms of address, warnings, symbols, etc.

I have also uploaded the blank dieline of the boxes

You are welcome and encouraged to also submit to projects 1, 3, 4, and 5 as well. The same rules and expectations apply.

Industry/Entity Type

It Company

Requirements
Should not have
• Should not have any images of an eye or any bionic/futuristic feel to the design
• Note that the stavolens box is for text reference only. You may use the lens image but the futuristic/bionic look is NOT what we are going for with this brand. It should be traditional upmarket medical device artwork.

```html
<!DOCTYPE html>
<html lang="en">
<head>
<meta charset="utf-8">
<title>Venmira – Tordel Vision intraocular lens packaging</title>
<link href="https://fonts.googleapis.com/css2?family=Montserrat:wght@400;600;700&display=swap" rel="stylesheet">
<style>
  :root {
    --navy: #12275a;
    --sky: #a9d2e8;
    --panel: #ffffff;
    --stage: #f1f3f5;
    --lens-light: #f3f7f9;
    --lens-mid: #dbe6ec;
    --lens-deep: #c3d3dc;
    --ink-on-navy: #ffffff;
  }
  * { margin: 0; padding: 0; box-sizing: border-box; }
  html, body {
    width: 1200px; height: 901px; overflow: hidden;
    background: var(--stage);
    font-family: "Montserrat", Arial, sans-serif;
  }
  .carton {
    position: absolute; left: 60px; top: 150px;
    display: flex; height: 600px;
    box-shadow: 0 10px 30px rgba(18, 39, 90, 0.10);
  }
  .carton-front {
    position: relative; width: 880px; height: 600px;
    background: var(--panel);
  }
  .carton-side {
    position: relative; width: 200px; height: 600px;
    background: var(--navy);
  }

  /* front panel */
  .brand {
    position: absolute; left: 60px; top: 140px;
    display: flex; align-items: center; gap: 14px;
  }
  .brand-dot {
    width: 22px; height: 22px; border-radius: 50%;
    background: var(--sky);
  }
  .brand-name {
    color: var(--navy); font-weight: 600;
    font-size: 28px; letter-spacing: 3px; text-transform: uppercase;
  }
  .product {
    position: absolute; left: 470px; top: 45px; width: 380px;
    color: var(--navy);
  }
  .product-name {
    font-size: 56px; font-weight: 600; letter-spacing: 5px;
    text-transform: uppercase; line-height: 1; padding: 0 0 16px 6px;
  }
  .product-rule { height: 2px; background: var(--navy); }
  .product-use {
    font-size: 21px; line-height: 1.3; padding: 12px 0 14px;
    text-align: center;
  }
  .product-use strong { font-weight: 700; }
  .lens-render {
    position: absolute; left: 110px; top: 215px;
    width: 520px; height: 270px; border-radius: 24px;
    background: linear-gradient(160deg, var(--lens-light), var(--lens-mid) 60%, var(--lens-deep));
  }
  .lens-profile {
    position: absolute; left: 110px; top: 515px;
    width: 520px; height: 22px; border-radius: 11px;
    background: linear-gradient(90deg, var(--lens-mid), var(--lens-deep), var(--lens-mid));
  }

  /* side panel */
  .side-symbols {
    position: absolute; right: 26px; top: 40px;
    display: flex; flex-direction: column; align-items: center; gap: 22px;
  }
  .side-symbol {
    width: 22px; height: 22px; border: 1.5px solid var(--ink-on-navy);
    border-radius: 50%; opacity: 0.75;
  }
  .side-symbol.is-square { border-radius: 2px; }
  .side-brand {
    position: absolute; left: 50%; bottom: 40px;
    transform-origin: left center;
    transform: translateX(-20px) rotate(90deg) translateX(-100%);
    display: flex; align-items: center; gap: 12px; white-space: nowrap;
  }
  .side-brand-dot {
    width: 18px; height: 18px; border-radius: 50%; background: var(--sky);
  }
  .side-brand-name {
    color: var(--ink-on-navy); font-weight: 600;
    font-size: 30px; letter-spacing: 3px; text-transform: uppercase;
  }
</style>
</head>
<body>
  <div class="carton">
    <main class="carton-front">
      <div class="brand">
        <span class="brand-dot"></span>
        <span class="brand-name">Tordel Vision</span>
      </div>

      <section class="product">
        <h1 class="product-name">Venmira</h1>
        <div class="product-rule"></div>
        <p class="product-use"><strong>Intraocular lens</strong> for use<br>in cataract surgery</p>
        <div class="product-rule"></div>
      </section>

      <div class="lens-render" role="img" aria-label="Rendered intraocular lens with curved haptics, front view"></div>
      <div class="lens-profile" role="img" aria-label="Rendered intraocular lens, side profile"></div>
    </main>

    <aside class="carton-side">
      <div class="side-symbols">
        <span class="side-symbol"></span>
        <span class="side-symbol"></span>
        <span class="side-symbol"></span>
        <span class="side-symbol is-square"></span>
        <span class="side-symbol is-square"></span>
      </div>
      <div class="side-brand">
        <span class="side-brand-dot"></span>
        <span class="side-brand-name">Tordel Vision</span>
      </div>
    </aside>
  </div>
</body>
</html>
```